BRISLEY Homes business card Coral Press

I've been a Real Estate agent since 1988. I left the BIG brokerages 2 years ago and am on my own and need a business card. I love doing graphics, but don't have the bandwidth right now.

Background. I want a card that stands out like I do. I'm the fun guy that always has a joke or funny story, and my clients like me. Something fun, but not too silly.

I don't have a symbol or logo that I'm using on the card now, but need to include something, a Font by itself or a logo? I'm not sure if we need a logo or not. I'm open.
The GREAT design is going to be the basis for the next project of stationary, note pads, and Real Estate FOR SALE & Open House signs.

Single sided card is fine, but I selected a 2 sided just in case that's what it works out to be.

Here we go. If you need anything else. Please let me know. As I think of anything, I'll add that also.

Target Market(s)

My territory is Santa Clara County / Silicon Valley, CA. I tend to work with new buyers buying a condo ($500,000) up to single family home for about $1.5 million. 1st time buyers and also move-up buyers. I haven't worked with multi-million $$ homes .... but wouldn't turn it down. Clients here tend to be White, Latin and now many more Chinese and East Indians. Clients also tend to be high tech, Zentrix, Quill, Mingleverse workers and also non tech people.

Industry/Entity Type

Business

Contact Information for Business Card

CONTENT:
Company: BRISLEY Homes
My name: Harold P. Brisley Jr.
Title: Real Estate Broker
Email: Hal@HaroldBrisley.example
Website: www.HaroldBrisley.example
Phone: (408) 555-0172
BRE # 07390418

Font styles to use
Sans Serif

Requirements
Must have
• Content from above. Something that stands out from the others. Serious enough looking, not stale, maybe a bit fun.

```html
<!DOCTYPE html>
<html lang="en">
<head>
<meta charset="utf-8">
<title>BRISLEY Homes — Business Card</title>
<link rel="stylesheet" href="https://fonts.googleapis.com/css2?family=Oswald:wght@400;500;600&family=Roboto:wght@500;700&display=swap">
<style>
  :root {
    --backdrop: #e9e6e2;
    --card-white: #f7f7f7;
    --card-black: #151515;
    --card-black-edge: #262626;
    --brand-red: #c8202a;
    --soft-red: #e2545b;
    --ink-dark: #2e2e2e;
    --ink-grey: #5a5a5a;
    --band-dark: #3a3a3a;
  }
  * { box-sizing: border-box; margin: 0; padding: 0; }
  html, body { width: 1200px; height: 871px; overflow: hidden; }
  body {
    background: var(--backdrop);
    display: flex;
    flex-direction: column;
    align-items: center;
    justify-content: center;
    gap: 56px;
    font-family: "Roboto", Arial, sans-serif;
  }
  .card {
    position: relative;
    width: 630px;
    height: 360px;
    border-radius: 4px;
    overflow: hidden;
    box-shadow: 0 10px 28px rgba(0,0,0,.22);
  }

  /* Front */
  .card--front { background: var(--card-white); }
  .front__brand {
    position: absolute;
    left: 48px; top: 118px;
    width: 250px;
    display: flex; align-items: center; gap: 12px;
  }
  .brand-square {
    width: 26px; height: 26px;
    background: var(--soft-red);
    flex: none;
  }
  .brand-name {
    font-family: "Oswald", Arial, sans-serif;
    font-weight: 500;
    font-size: 30px;
    letter-spacing: 3px;
    color: var(--ink-grey);
    white-space: nowrap;
  }
  .front__divider {
    position: absolute;
    left: 318px; top: 62px;
    width: 2px; height: 150px;
    background: var(--soft-red);
  }
  .front__details {
    position: absolute;
    left: 342px; top: 60px;
  }
  .agent-name {
    font-family: "Oswald", Arial, sans-serif;
    font-weight: 600;
    font-size: 24px;
    color: var(--ink-grey);
    letter-spacing: .5px;
    line-height: 1.1;
  }
  .agent-title {
    font-weight: 700;
    font-size: 15px;
    color: var(--soft-red);
    margin-bottom: 8px;
  }
  .contact-line {
    display: flex; align-items: center; gap: 9px;
    font-weight: 700;
    font-size: 14px;
    color: var(--ink-dark);
    line-height: 1.75;
  }
  .contact-line svg { width: 14px; height: 12px; fill: var(--soft-red); flex: none; }
  .license {
    font-weight: 700;
    font-size: 16px;
    color: var(--brand-red);
    letter-spacing: 1px;
    margin-top: 4px;
  }
  .front__band {
    position: absolute;
    left: 0; right: 0; bottom: 0;
    height: 70px;
  }

  /* Back */
  .card--back {
    background: radial-gradient(ellipse at 50% 40%, var(--card-black-edge) 0%, var(--card-black) 70%);
    display: flex; flex-direction: column; align-items: center; justify-content: center;
    gap: 34px;
  }
  .back__brand { display: flex; align-items: center; gap: 16px; }
  .back__brand .brand-square { width: 34px; height: 34px; background: var(--brand-red); }
  .back__brand .brand-name {
    font-size: 44px;
    letter-spacing: 6px;
    color: var(--soft-red);
  }
  .website {
    font-family: "Oswald", Arial, sans-serif;
    font-weight: 400;
    font-size: 26px;
    letter-spacing: 2px;
    color: var(--brand-red);
  }
</style>
</head>
<body>
  <section class="card card--front" aria-label="Card front">
    <div class="front__brand">
      <span class="brand-square"></span>
      <span class="brand-name">BRISLEY Homes</span>
    </div>
    <div class="front__divider"></div>
    <div class="front__details">
      <p class="agent-name">Harold P. Brisley Jr.</p>
      <p class="agent-title">Real Estate Broker</p>
      <p class="contact-line">
        <svg viewBox="0 0 14 12" aria-hidden="true"><path d="M1 3 Q7 -1 13 3 L12 5 L10 4 L10 6 L12 8 L12 12 L2 12 L2 8 L4 6 L4 4 L2 5 Z"/></svg>
        (408) 555-0172
      </p>
      <p class="contact-line">
        <svg viewBox="0 0 14 12" aria-hidden="true"><path d="M0 2 H14 V12 H0 Z M1 3 L7 8 L13 3" stroke="#f7f7f7" stroke-width="1"/></svg>
        Hal@HaroldBrisley.example
      </p>
      <p class="license">BRE # 07390418</p>
    </div>
    <svg class="front__band" viewBox="0 0 630 70" preserveAspectRatio="none" aria-hidden="true">
      <polygon points="0,52 630,40 630,70 0,70" fill="var(--soft-red)"/>
      <polygon points="0,58 630,48 630,70 0,70" fill="var(--brand-red)"/>
      <polygon points="330,30 420,28 410,46 320,48" fill="var(--band-dark)"/>
      <polygon points="430,27 630,23 630,38 420,42" fill="var(--brand-red)"/>
    </svg>
  </section>

  <section class="card card--back" aria-label="Card back">
    <div class="back__brand">
      <span class="brand-square"></span>
      <span class="brand-name">BRISLEY Homes</span>
    </div>
    <p class="website">www.HaroldBrisley.example</p>
  </section>
</body>
</html>
```